Boot Camp Flyer

Outdoor Boot Camp
SAMPLE DESIGNS I LIKE UPLOADED.
Similar to this or be creative !
I need A5 and DL flyer promoting our Boot Camp program, similar to the sample design but include our details. Pink blue green black white yellow and purple colours ok

PRICE: $100
WHEN: Thursdays & Saturdays
Thursday 6pm
Saturday 9am

WHERE: Brindle Paddock

Get results all year round! 5 week boot camp only $100
Join in any time! Register your place now!

Tone Fast Boot Camp
Register now at kestrelmovement@mailbox.example or www.social.example/kestrelmovementnz
Female only. Registration essential. ALL fitness levels welcome.

Conditions
Valid from Mar 22, 2018
Expires 26th Apr, 2018
Register online. Subject to availability. Valid for new clients only. Valid for unlimited sessions per week. Boot Camps run in 5 week blocks. Non-transferable. No refunds unless required by law. No cashback. Not to be used with any other offer.

Could maybe write 5 week tone fast challenge

Target Market(s)

Female 20s-40s

Industry/Entity Type

Fitness

Colors

Designer to choose colors to be used in the design.

Requirements
Must have
• Colour
• Easy to read font
• Picture of females (target market) exercising
Nice to have
• Terms and conditions in small print down bottom.
Should not have
• Too much text

```html
<!DOCTYPE html>
<html lang="en">
<head>
<meta charset="utf-8">
<title>Tone Fast Boot Camp Flyer</title>
<link rel="stylesheet" href="https://fonts.googleapis.com/css2?family=Anton&family=Oswald:wght@400;500;700&family=Roboto+Condensed:wght@400;700&display=swap">
<style>
  :root {
    --bg: #15181c;
    --pink: #e5177e;
    --green: #2bb24c;
    --blue: #1ba1d8;
    --band-grey: #d8d9db;
    --ink-dark: #24272b;
    --white: #ffffff;
    --muted: #9a9ea4;
  }
  * { margin: 0; padding: 0; box-sizing: border-box; }
  html, body { width: 849px; height: 1200px; overflow: hidden; background: var(--bg); }
  .flyer {
    position: relative; width: 849px; height: 1200px; overflow: hidden;
    background: var(--bg); color: var(--white);
    font-family: "Roboto Condensed", Arial, sans-serif;
  }
  .art { position: absolute; inset: 0; }
  .offer { position: absolute; right: 30px; top: 28px; text-align: right; font-family: "Oswald", sans-serif; }
  .offer-weeks { font-size: 44px; font-weight: 700; line-height: 1; }
  .offer-name { font-size: 25px; font-weight: 500; letter-spacing: 1px; margin-top: 6px; }
  .offer-price { font-size: 76px; font-weight: 700; color: var(--pink); line-height: 1; margin-top: 8px; }
  .schedule { position: absolute; left: 40px; top: 580px; width: 470px; text-align: center; font-family: "Oswald", sans-serif; }
  .schedule-days { font-size: 28px; font-weight: 400; }
  .schedule-dates { font-size: 40px; font-weight: 700; margin-top: 2px; }
  .schedule-dates sup { font-size: 19px; }
  .sessions { display: flex; margin-top: 14px; }
  .session { flex: 1; font-size: 27px; padding: 4px 0; white-space: nowrap; }
  .session b { font-weight: 700; margin-left: 10px; }
  .session-thu { background: var(--green); }
  .session-sat { background: var(--blue); }
  .venue { font-size: 26px; font-weight: 500; margin-top: 12px; }
  .features { position: absolute; left: 586px; top: 582px; list-style: none; font-size: 21px; line-height: 1.7; white-space: nowrap; }
  .features li::before { content: "\25B8"; margin-right: 9px; }
  .footer { position: absolute; left: 0; right: 0; top: 1080px; height: 120px; }
  .footer-pitch { position: absolute; left: 40px; top: 10px; width: 300px; font-size: 16px; line-height: 1.3; text-align: center; }
  .footer-contact { position: absolute; left: 380px; top: 10px; font-size: 16px; line-height: 1.3; }
  .footer-contact .link { color: var(--pink); font-weight: 700; }
  .brand { position: absolute; right: 30px; top: 6px; display: flex; flex-direction: column; align-items: center; gap: 6px;
    font-family: "Roboto Condensed", sans-serif; font-weight: 700; font-size: 15px; color: var(--white); }
  .brand-dot { width: 24px; height: 24px; border-radius: 50%; background: var(--pink); }
  .fine-print { position: absolute; left: 40px; right: 30px; top: 84px; font-size: 9px; line-height: 1.3; color: var(--muted); }
</style>
</head>
<body>
<div class="flyer">
  <svg class="art" width="849" height="1200" viewBox="0 0 849 1200">
    <defs>
      <linearGradient id="heroTone" x1="0" y1="0" x2="1" y2="1">
        <stop offset="0" stop-color="#8b8f95"/>
        <stop offset="0.55" stop-color="#3d4045"/>
        <stop offset="1" stop-color="#15181c"/>
      </linearGradient>
      <linearGradient id="floorTone" x1="0" y1="0" x2="1" y2="0">
        <stop offset="0" stop-color="#15181c"/>
        <stop offset="0.35" stop-color="#1f5a6a"/>
        <stop offset="0.7" stop-color="#4a2a5e"/>
        <stop offset="1" stop-color="#15181c"/>
      </linearGradient>
    </defs>
    <rect x="0" y="0" width="849" height="570" fill="url(#heroTone)" role="img" aria-label="Photo of a woman lifting dumbbells in a workout"/>
    <rect x="0" y="800" width="849" height="280" fill="url(#floorTone)" role="img" aria-label="Photo of a woman doing a push-up"/>
    <g transform="rotate(-10 620 400)">
      <rect x="400" y="335" width="520" height="125" fill="var(--band-grey)"/>
      <text x="625" y="436" text-anchor="middle" font-family="Anton, sans-serif" font-size="80" fill="var(--ink-dark)">BOOTCAMP</text>
    </g>
    <g transform="rotate(-10 220 450)">
      <rect x="-40" y="500" width="480" height="10" fill="var(--blue)"/>
      <rect x="-40" y="395" width="480" height="106" fill="var(--pink)"/>
      <text x="215" y="481" text-anchor="middle" font-family="Anton, sans-serif" font-size="80" fill="var(--white)">TONE FAST</text>
    </g>
  </svg>

  <div class="offer">
    <div class="offer-weeks">5 WEEK</div>
    <div class="offer-name">TONE FAST CHALLENGE</div>
    <div class="offer-price">$100</div>
  </div>

  <div class="schedule">
    <div class="schedule-days">Thursdays &amp; Saturdays</div>
    <div class="schedule-dates">22<sup>nd</sup> March - 26<sup>th</sup> April</div>
    <div class="sessions">
      <div class="session session-thu">Thursday <b>| 6pm</b></div>
      <div class="session session-sat">Saturday <b>| 9am</b></div>
    </div>
    <div class="venue">Brindle Paddock</div>
  </div>

  <ul class="features">
    <li>Female only</li>
    <li>Registration essential</li>
    <li>ALL fitness levels welcome</li>
  </ul>

  <div class="footer">
    <div class="footer-pitch">Get results all year round!<br>5 week boot camp only $100.<br>Join in any time! <b>Register your place now!</b></div>
    <div class="footer-contact">Register now at<br><span class="link">kestrelmovement@mailbox.example</span><br><span class="link">www.social.example/kestrelmovementnz</span></div>
    <div class="brand"><span class="brand-dot"></span>Kestrel Movement</div>
    <div class="fine-print">*conditions apply. Valid from Mar 22, 2018. Expires 26th Apr, 2018. Register online. Subject to availability. Valid for new clients only. Valid for unlimited sessions per week. Boot Camps run in 5 week blocks. Non-transferable. No refunds unless required by law. No cashback. Not to be used with any other offer.</div>
  </div>
</div>
</body>
</html>
```